ROVE Poster

-Poster to advertise the Ridge Outdoor Venture Excursion
- we would like to be able to print as large as possible but for the most part, 18x24 inches should be fine.
-For more information and pics of the programs please visit our fb page:
www.friendspage.net/ROVEWestward
- we can also email more pics if requested (please email roveon@trailpost,net

Target Market(s)

students (age 14-22) and parents

Industry/Entity Type

Leadership

Requirements
Must have
• 1. our contact info (www.wildschool.td82.vx.net and 1-729-583-1862)
2. One of each of our supporting logos (Crest Award, TD82, oarsmen guild)
3. "ROVE offers secondary students an applied field-course in Leadership Studies. During this 9 day outdoor immersion, students will develop their Action-Centered leadership skills. The climax of ROVE is the Journey, which is taken through a modality of choice (Tidewise, Timberline, Glide). ROVE is a transformative passage where learners develop a deeper relational understanding of themselves within the greater cultural and biological ecology of the Pacific Northwest.
Nice to have
• A image that represents each Journey (Tidewise, Timberline, Glide) and corresponding description:
a. ROVE Tidewise: Explore marine ecosystems of the Salish Sea while learning to sail aboard a 53’Schooner
Optional Certificate: Pleasure Operators Card and Sailing Level1
b. ROVE Timberline: Follow in the footsteps of the Canada’s Fur Traders as you explore the Coast Mountain wilderness along the Ferncliff Lakes Paddle Trail Optional Certificate: Canoe Skills Intermediate Certificate
c. ROVE Glide: Dig deep into the traditional Hawaiian practice of Stand-Up Paddle Boarding while exploring the sheltered waters of Desolation Sound
Optional Certificate: Glide Advanced Skills

notes:
-We have combined and batched pics so we could include as many as possible.
-They are batched according to use (photos, logos, support logos).
-Not all pics/logos need to be used.
-We wanted to allow you the flexibility.
-We can also provide more by request.

If you require supplemental materials please email roveon@trailpost.net

Thanks so much,
ROVE team

```html
<!DOCTYPE html>
<html lang="en">
<head>
<meta charset="utf-8">
<title>ROVE Poster</title>
<link href="https://fonts.googleapis.com/css2?family=Lato:wght@300;400;700&family=Open+Sans:wght@400;600;700&display=swap" rel="stylesheet">
<style>
  :root {
    --page-bg: #ececec;
    --cream: #f6f1cb;
    --forest: #0f4744;
    --rust: #9d1c15;
    --gold: #eed84a;
    --ink: #1c1c1c;
    --body-text: #5a5a52;
    --white: #ffffff;
  }
  * { margin: 0; padding: 0; box-sizing: border-box; }
  html, body {
    width: 1200px; height: 849px; overflow: hidden;
    background: var(--page-bg);
  }
  .poster {
    position: absolute;
    left: 331px; top: 72px;
    width: 524px; height: 698px;
    transform: scale(1.0265);
    transform-origin: 0 0;
    background: var(--cream);
    font-family: "Lato", sans-serif;
    color: var(--ink);
  }
  .brand {
    position: absolute; left: 33px; top: 120px; width: 210px;
    text-align: center;
  }
  .brand-mark {
    display: inline-block; width: 14px; height: 14px;
    background: var(--ink); border-radius: 50%;
    margin-bottom: 6px;
  }
  .brand-name {
    font-family: "Lato", sans-serif; font-weight: 300;
    font-size: 50px; line-height: 1; letter-spacing: 1px;
    color: var(--ink);
  }
  .brand-tagline {
    font-size: 8px; font-weight: 400; margin-top: 3px; color: var(--ink);
  }
  .color-bar {
    position: absolute; left: 33px; top: 215px; height: 18px; width: 210px;
    display: flex;
  }
  .color-bar span:nth-child(1) { width: 65px; background: var(--forest); }
  .color-bar span:nth-child(2) { width: 77px; background: var(--rust); }
  .color-bar span:nth-child(3) { width: 68px; background: var(--gold); }
  .intro {
    position: absolute; left: 262px; top: 40px; width: 232px;
    font-size: 10.6px; line-height: 20.3px; font-weight: 300;
    color: var(--body-text);
  }
  .intro strong { font-weight: 700; color: var(--body-text); }
  .journeys {
    position: absolute; left: 0; top: 284px; width: 524px;
    display: grid; grid-template-columns: 175px 174px 175px;
  }
  .journey-photo { height: 156px; }
  .photo-tidewise { background: linear-gradient(180deg, #a9b3b8 0%, #8c8f8a 40%, #c0542c 65%, #3a3f4a 100%); }
  .photo-timberline { background: linear-gradient(180deg, #7fa6cc 0%, #b6cde0 30%, #3f5a3a 50%, #284030 68%, #cfd3d0 80%, #4a6676 100%); }
  .photo-glide { background: linear-gradient(180deg, #4f6390 0%, #3a4b78 45%, #1f2b48 60%, #2e3d66 100%); }
  .journey-card {
    height: 145px; padding: 22px 20px 0 33px; color: var(--white);
    font-family: "Open Sans", sans-serif;
  }
  .journey-card.tidewise { background: var(--forest); }
  .journey-card.timberline { background: var(--rust); }
  .journey-card.glide { background: var(--gold); }
  .journey-title { font-size: 13px; font-weight: 700; margin-bottom: 3px; }
  .journey-text { font-size: 7.4px; line-height: 10.4px; }
  .journey-cert { font-size: 7.4px; line-height: 10.4px; margin-top: 9px; }
  .journey-cert b { font-weight: 700; }
  .footer {
    position: absolute; left: 0; top: 585px; width: 524px; height: 113px;
  }
  .district {
    position: absolute; left: 35px; top: 31px; display: flex; align-items: center; gap: 8px;
  }
  .district-mark { width: 22px; height: 22px; background: var(--rust); }
  .district-name {
    font-family: "Open Sans", sans-serif; font-weight: 700; font-size: 10.5px;
    line-height: 13px; color: var(--rust);
  }
  .partner-badges { position: absolute; left: 276px; top: 28px; display: flex; gap: 24px; }
  .partner-badges svg { display: block; }
  .apply {
    position: absolute; right: 32px; top: 31px; text-align: right;
    font-family: "Open Sans", sans-serif; color: var(--ink);
  }
  .apply-heading { font-size: 13px; font-weight: 400; margin-bottom: 5px; }
  .apply-line { font-size: 7.4px; line-height: 10px; }
</style>
</head>
<body>
<main class="poster">
  <div class="brand">
    <span class="brand-mark"></span>
    <div class="brand-name">ROVE</div>
    <div class="brand-tagline">Ridge Outdoor Venture Excursion</div>
  </div>
  <div class="color-bar"><span></span><span></span><span></span></div>

  <p class="intro"><strong>ROVE</strong> offers secondary students an applied field-course in Leadership Studies. During this 9 day outdoor immersion, students will develop their Action-Centered leadership skills. The climax of <strong>ROVE</strong> is the Journey, which is taken through a modality of choice (Tidewise, Timberline, Glide). <strong>ROVE</strong> is a transformative passage where learners develop a deeper relational understanding of themselves within the greater cultural and biological ecology of the Pacific Northwest.</p>

  <section class="journeys">
    <div class="journey-photo photo-tidewise" role="img" aria-label="Students in life jackets aboard a schooner on the sea"></div>
    <div class="journey-photo photo-timberline" role="img" aria-label="Group in canoes on a mountain lake"></div>
    <div class="journey-photo photo-glide" role="img" aria-label="Paddler on a stand-up board at dusk"></div>

    <div class="journey-card tidewise">
      <h2 class="journey-title">ROVE Tidewise:</h2>
      <p class="journey-text">Explore marine ecosystems of the Salish Sea while learning to sail aboard a 53’Schooner</p>
      <p class="journey-cert"><b>Optional Certificate:</b><br>Pleasure Operators Card and Sailing Level 1</p>
    </div>
    <div class="journey-card timberline">
      <h2 class="journey-title">ROVE Timberline:</h2>
      <p class="journey-text">Follow in the footsteps of the Canada’s Fur Traders as you explore the Coast Mountain wilderness along the Ferncliff Lakes Paddle Trail</p>
      <p class="journey-cert"><b>Optional Certificate:</b><br>Canoe Skills Intermediate Certificate</p>
    </div>
    <div class="journey-card glide">
      <h2 class="journey-title">ROVE Glide:</h2>
      <p class="journey-text">Dig deep into the traditional Hawaiian practice of Stand-Up Paddle Boarding while exploring the sheltered waters of Desolation Sound</p>
      <p class="journey-cert"><b>Optional Certificate:</b><br>Glide Advanced Skills</p>
    </div>
  </section>

  <footer class="footer">
    <div class="district">
      <span class="district-mark"></span>
      <div class="district-name">Tidal District 82<br>Outdoor &amp; Ecological Learning</div>
    </div>
    <div class="partner-badges">
      <svg width="26" height="42" viewBox="0 0 26 42" role="img" aria-label="Crest Award badge"><rect x="1" y="1" width="24" height="40" rx="3" fill="#2b2b2b"/></svg>
      <svg width="16" height="42" viewBox="0 0 16 42" role="img" aria-label="Oarsmen Guild badge"><rect x="0" y="0" width="16" height="42" fill="#c8382a"/></svg>
    </div>
    <div class="apply">
      <div class="apply-heading">Apply here:</div>
      <div class="apply-line">www.wildschool.td82.vx.net</div>
      <div class="apply-line">1-729-583-1862</div>
    </div>
  </footer>
</main>
</body>
</html>
```